New Coffee Shop business card

We are opening our new coffee shop and are needing business cards to take with us on February 6th to Atlanta, Ga to a show.

We will be offering the following menu type items:

coffee
teas
espresso
frappes
smoothies

sandwiches
soups
salads
pastries
ice cream

Our shop is in a rural country-side area and we would like to convey that feel in our shop. In addition to the cafe we will also be selling gifts and furniture and other home decor. Much of this merchandise will be rescued, refurbished or repurposed which is also a core value of what we are all about.

We have a company logo we would like incorporated into the design.

We will also provide files that have the elements of the logo which may also be useful in the design of the card.

Since we are not open yet we need one slightly altered version of the card as well as the final product which states "Opening in the summer 2015"

Target Market(s)

moderate to slightly upscale and folksy.

Industry/Entity Type

Coffee Shop

Contact Information for Business Card

Fern Hollow Coffee
name
address
phone number
email

Card

Font styles to use
Sans Serif

Requirements
Must have
• Must include Logo
• Must include information on menu.
• Must include information on our merchandise sales as described inthe project description.
• Color scheme to complement the logo
Nice to have
• The following descriptions
• "We are also selling gifts, furniture, and other home decoration."
• "We rescue, refurbish, and repurpose old furniture so it can live again."

```html
<!DOCTYPE html>
<html lang="en">
<head>
<meta charset="utf-8">
<title>Fern Hollow Coffee — Business Cards</title>
<link rel="stylesheet" href="https://fonts.googleapis.com/css2?family=Jost:wght@400;500&display=swap">
<style>
  :root {
    --maroon: #7d1a22;
    --maroon-deep: #6a141b;
    --charcoal: #2b2b2d;
    --paper: #ffffff;
    --ink: #1e1e1e;
    --ghost: #e3e1df;
    --backdrop: #ece9e4;
  }
  * { box-sizing: border-box; margin: 0; padding: 0; }
  html, body { width: 1200px; height: 900px; overflow: hidden; }
  body {
    background: var(--backdrop);
    font-family: "Jost", Arial, sans-serif;
    position: relative;
  }
  .card {
    position: absolute;
    left: 250px;
    width: 700px;
    height: 400px;
    overflow: hidden;
    box-shadow: 0 6px 18px rgba(0,0,0,.18);
  }

  /* Front */
  .card--front { top: 35px; background: var(--maroon); color: var(--paper); text-align: center; }
  .front__announce { margin-top: 34px; font-size: 15px; letter-spacing: 1.5px; }
  .brand { display: flex; align-items: center; justify-content: center; gap: 14px; margin-top: 78px; }
  .brand__dot { width: 22px; height: 22px; border-radius: 50%; background: var(--paper); }
  .brand__name { font-size: 40px; font-weight: 400; letter-spacing: 1px; }
  .front__tagline { position: absolute; left: 0; right: 0; bottom: 46px; font-size: 17px; line-height: 1.35; letter-spacing: .4px; }

  /* Back */
  .card--back { top: 465px; background: var(--paper); color: var(--ink); }
  .back__watermark {
    position: absolute; left: 222px; top: 272px;
    font-size: 44px; line-height: 50px; color: var(--ghost); letter-spacing: 1px; white-space: nowrap;
  }
  .menu { position: absolute; left: 42px; top: 38px; list-style: none; }
  .menu__item { display: flex; align-items: center; gap: 10px; font-size: 19px; line-height: 26.5px; letter-spacing: .6px; }
  .menu__item svg { width: 14px; height: 16px; flex: none; }
  .address { position: absolute; right: 40px; top: 34px; text-align: right; font-size: 14.5px; line-height: 18px; }
  .person { position: absolute; right: 60px; top: 112px; text-align: right; }
  .person__name { color: var(--maroon); font-size: 21px; letter-spacing: .5px; }
  .person__role { font-size: 14px; margin-right: -6px; }
  .contacts { position: absolute; right: 30px; top: 180px; list-style: none; text-align: right; }
  .contacts li { display: flex; justify-content: flex-end; align-items: center; gap: 8px; font-size: 15.5px; line-height: 21px; }
  .contacts svg { width: 15px; height: 14px; flex: none; }
  .band { position: absolute; left: 0; bottom: 0; width: 100%; height: 62px; }
</style>
</head>
<body>

<section class="card card--front" aria-label="Card front">
  <p class="front__announce">OPENING IN THE SUMMER 2015</p>
  <div class="brand">
    <span class="brand__dot"></span>
    <span class="brand__name">Fern Hollow Coffee</span>
  </div>
  <p class="front__tagline">
    We are also selling gifts, furniture, and other home decoration<br>
    We rescue, refurbish, and repurpose old furniture so it can live again
  </p>
</section>

<section class="card card--back" aria-label="Card back">
  <span class="back__watermark" aria-hidden="true">Fern Hollow Coffee</span>

  <ul class="menu">
    <li class="menu__item"><svg viewBox="0 0 14 16"><path d="M4 1c-1 2 1 3 0 5M8 1c-1 2 1 3 0 5" stroke="#7d1a22" fill="none" stroke-width="1"/><path d="M1 9h10v3a3 3 0 0 1-3 3H4a3 3 0 0 1-3-3z M11 10h2v2h-2" fill="#7d1a22"/></svg>COFFEE</li>
    <li class="menu__item"><svg viewBox="0 0 14 16"><path d="M4 1c-1 2 1 3 0 5M8 1c-1 2 1 3 0 5" stroke="#7d1a22" fill="none" stroke-width="1"/><path d="M1 9h10v3a3 3 0 0 1-3 3H4a3 3 0 0 1-3-3z M11 10h2v2h-2" fill="#7d1a22"/></svg>TEAS</li>
    <li class="menu__item"><svg viewBox="0 0 14 16"><path d="M4 1c-1 2 1 3 0 5M8 1c-1 2 1 3 0 5" stroke="#7d1a22" fill="none" stroke-width="1"/><path d="M1 9h10v3a3 3 0 0 1-3 3H4a3 3 0 0 1-3-3z M11 10h2v2h-2" fill="#7d1a22"/></svg>ESPRESSO</li>
    <li class="menu__item"><svg viewBox="0 0 14 16"><path d="M4 1c-1 2 1 3 0 5M8 1c-1 2 1 3 0 5" stroke="#7d1a22" fill="none" stroke-width="1"/><path d="M1 9h10v3a3 3 0 0 1-3 3H4a3 3 0 0 1-3-3z M11 10h2v2h-2" fill="#7d1a22"/></svg>FRAPPES</li>
    <li class="menu__item"><svg viewBox="0 0 14 16"><path d="M4 1c-1 2 1 3 0 5M8 1c-1 2 1 3 0 5" stroke="#7d1a22" fill="none" stroke-width="1"/><path d="M1 9h10v3a3 3 0 0 1-3 3H4a3 3 0 0 1-3-3z M11 10h2v2h-2" fill="#7d1a22"/></svg>SMOOTHIES</li>
    <li class="menu__item"><svg viewBox="0 0 14 16"><path d="M4 1c-1 2 1 3 0 5M8 1c-1 2 1 3 0 5" stroke="#7d1a22" fill="none" stroke-width="1"/><path d="M1 9h10v3a3 3 0 0 1-3 3H4a3 3 0 0 1-3-3z M11 10h2v2h-2" fill="#7d1a22"/></svg>SANDWICHES</li>
    <li class="menu__item"><svg viewBox="0 0 14 16"><path d="M4 1c-1 2 1 3 0 5M8 1c-1 2 1 3 0 5" stroke="#7d1a22" fill="none" stroke-width="1"/><path d="M1 9h10v3a3 3 0 0 1-3 3H4a3 3 0 0 1-3-3z M11 10h2v2h-2" fill="#7d1a22"/></svg>SOUPS</li>
    <li class="menu__item"><svg viewBox="0 0 14 16"><path d="M4 1c-1 2 1 3 0 5M8 1c-1 2 1 3 0 5" stroke="#7d1a22" fill="none" stroke-width="1"/><path d="M1 9h10v3a3 3 0 0 1-3 3H4a3 3 0 0 1-3-3z M11 10h2v2h-2" fill="#7d1a22"/></svg>SALADS</li>
    <li class="menu__item"><svg viewBox="0 0 14 16"><path d="M4 1c-1 2 1 3 0 5M8 1c-1 2 1 3 0 5" stroke="#7d1a22" fill="none" stroke-width="1"/><path d="M1 9h10v3a3 3 0 0 1-3 3H4a3 3 0 0 1-3-3z M11 10h2v2h-2" fill="#7d1a22"/></svg>PASTRIES</li>
    <li class="menu__item"><svg viewBox="0 0 14 16"><path d="M4 1c-1 2 1 3 0 5M8 1c-1 2 1 3 0 5" stroke="#7d1a22" fill="none" stroke-width="1"/><path d="M1 9h10v3a3 3 0 0 1-3 3H4a3 3 0 0 1-3-3z M11 10h2v2h-2" fill="#7d1a22"/></svg>ICE CREAM</li>
  </ul>

  <p class="address">14 Mill Creek Road,<br>Ellijay, GA, 30540</p>

  <div class="person">
    <p class="person__name">CLARA WHITFIELD</p>
    <p class="person__role">Manager</p>
  </div>

  <ul class="contacts">
    <li>+1 706 555 0148 <svg viewBox="0 0 15 14"><path d="M3 1l3 3-2 2c1 2 2 3 4 4l2-2 3 3-2 2C6 13 2 9 1 3z" fill="#7d1a22"/></svg></li>
    <li>+1 706 555 0192 <svg viewBox="0 0 15 14"><rect x="4" y="0.5" width="7" height="13" rx="1.2" fill="none" stroke="#7d1a22" stroke-width="1.3"/><circle cx="7.5" cy="11" r=".9" fill="#7d1a22"/></svg></li>
    <li>clara@fernhollow.com <svg viewBox="0 0 15 14"><rect x="0.5" y="2" width="14" height="10" fill="#7d1a22"/><path d="M1 2.5l6.5 5 6.5-5" stroke="#fff" fill="none" stroke-width="1.2"/></svg></li>
    <li>www.fernhollow.com <svg viewBox="0 0 15 14"><rect x="0.7" y="0.7" width="13.6" height="9" fill="none" stroke="#7d1a22" stroke-width="1.3"/><path d="M5 13h5M7.5 10v3" stroke="#7d1a22" stroke-width="1.3"/></svg></li>
  </ul>

  <svg class="band" viewBox="0 0 700 62" preserveAspectRatio="none" aria-hidden="true">
    <polygon points="0,62 0,30 520,0 520,62" fill="var(--maroon)"/>
    <polygon points="530,0 700,0 700,62 530,62" fill="var(--charcoal)"/>
    <polygon points="520,62 520,0 530,0 530,62" fill="#fff"/>
  </svg>
</section>

</body>
</html>
```